Judicial election website to attract voters

I need a simple one-page web design for a judicial election. I'm going to put up one picture, maybe two. The picture I have needs a little touch-up (whiten teeth for example). I have 3 paragraphs of text. I'd like a "Donate" button that can link to a CoinDrift account. I'd also like a little background design, like the Constitution or something like that. There's a couple other little things but that's the bulk of it.

Target Market(s)

Involved voters and some media

Industry/Entity Type

Legal

Number of Pages Required

1 page

Font styles to use
Sans Serif

Requirements
Must have
• My picture, text, donate button
• Phrase "Remember to vote August 30, 2016!"
Nice to have
• Perhaps a second photo, maybe a short 30 second video of me talking directly to the voters, cool background: Constitution, something judgey.
Should not have
• Not sure ... profanity, I guess.

```html
<!DOCTYPE html>
<html lang="en">
<head>
<meta charset="utf-8">
<title>Remember to vote August 30, 2016!</title>
<link rel="stylesheet" href="https://fonts.googleapis.com/css2?family=Lato:wght@300;400;700&family=Zilla+Slab:wght@700&display=swap">
<style>
  :root {
    --coral: #f4504f;
    --coral-text: #ef4a4b;
    --hero-light: #f1f1f1;
    --hero-mid: #e4e4e4;
    --ink: #4a4a4a;
    --white: #ffffff;
    --photo-light: #f6f1ee;
    --photo-warm: #e9b9a6;
  }
  * { box-sizing: border-box; margin: 0; padding: 0; }
  html, body { width: 1200px; height: 1152px; overflow: hidden; }
  body { position: relative; font-family: "Lato", sans-serif; background: var(--coral); }

  .hero { position: absolute; left: 0; top: 0; width: 1200px; height: 544px; overflow: hidden; }
  .hero-backdrop {
    position: absolute; inset: 0;
    background:
      radial-gradient(ellipse 500px 320px at 620px 360px, #f7f7f7 0%, rgba(247,247,247,0) 100%),
      linear-gradient(160deg, var(--hero-mid) 0%, var(--hero-light) 45%, var(--hero-mid) 100%);
  }
  .top-nav { position: absolute; top: 50px; right: 92px; display: flex; align-items: center; gap: 42px; }
  .donate-link {
    display: flex; align-items: center; gap: 7px;
    font-family: "Zilla Slab", serif; font-weight: 700; font-size: 25px;
    color: var(--coral-text); text-decoration: none;
  }
  .donate-dot { width: 13px; height: 13px; border-radius: 50%; background: var(--coral-text); }
  .menu-toggle { width: 24px; height: 20px; display: block; }

  .hero-title {
    position: absolute; left: 198px; top: 168px;
    font-weight: 700; font-size: 42px; letter-spacing: -0.3px; color: var(--coral-text);
  }
  .hero-contact {
    position: absolute; left: 198px; top: 245px;
    font-weight: 300; font-size: 21.5px; color: var(--ink);
  }
  .about-button {
    position: absolute; left: 199px; top: 335px; width: 157px; height: 64px;
    background: var(--white); border-radius: 0 32px 32px 0;
    display: flex; align-items: center; gap: 10px; padding-left: 15px;
    font-family: "Zilla Slab", serif; font-weight: 700; font-size: 24px;
    color: var(--coral-text); text-decoration: none;
    box-shadow: 0 2px 8px rgba(0,0,0,0.06);
  }
  .about-icon { width: 12px; height: 12px; border-radius: 50%; background: var(--coral-text); }

  .bio { position: absolute; left: 0; top: 544px; width: 1200px; height: 608px; background: var(--coral); }
  .bio-heading {
    position: absolute; left: 198px; top: 124px;
    font-weight: 700; font-size: 39px; color: var(--white); letter-spacing: -0.3px;
  }
  .bio-text {
    position: absolute; left: 198px; top: 196px; width: 412px;
    font-weight: 300; font-size: 18.5px; line-height: 41.4px; color: var(--white);
  }
  .candidate-photo {
    position: absolute; left: 661px; top: 70px; width: 406px; height: 538px;
    background:
      radial-gradient(ellipse 150px 190px at 200px 270px, #e6d2c4 0%, rgba(230,210,196,0) 100%),
      linear-gradient(180deg, var(--photo-light) 0%, #efe7e2 65%, var(--photo-warm) 100%);
  }
</style>
</head>
<body>
  <header class="hero">
    <div class="hero-backdrop" role="img" aria-label="Faded background of old constitutional parchment scrolls, a quill pen and scattered stars"></div>
    <nav class="top-nav">
      <a class="donate-link" href="#" aria-label="Donate with CoinDrift"><span class="donate-dot"></span>donate</a>
      <svg class="menu-toggle" viewBox="0 0 24 20" aria-label="Menu">
        <rect x="0" y="0" width="24" height="3.4" rx="1" fill="#ef4a4b"/>
        <rect x="0" y="8.3" width="24" height="3.4" rx="1" fill="#ef4a4b"/>
        <rect x="0" y="16.6" width="24" height="3.4" rx="1" fill="#ef4a4b"/>
      </svg>
    </nav>
    <h1 class="hero-title">Remember to vote August 30, 2016!</h1>
    <p class="hero-contact">I am reachable at marianne@votemarianne.org</p>
    <a class="about-button" href="#about"><span class="about-icon"></span>about me</a>
  </header>

  <section class="bio" id="about">
    <h2 class="bio-heading">EXPERIENCED</h2>
    <p class="bio-text">Marianne was born and raised in Tampa Florida, the daughter of an air-conditioning repairman who later opened his own successful business. As the first in her family to go to college, her parents could not have been more proud as she finished her degree at Gulf Coast University, then continued on to Bayshore State University School of Law where she graduated with honors.</p>
    <div class="candidate-photo" role="img" aria-label="Portrait photograph of the candidate smiling, on a white background"></div>
  </section>
</body>
</html>
```